Fernhollow Co Website Design

We are working with a water product retailer in Washington called Fernhollow Co.

Some sites to use for content/competitors and inspiration:

https://www.brivelto.com
https://tanmoril.example/designs/retail/ (lots of retail website designs we've approved and continue to show clients)

Thank you for taking the time to consider designing a website for us. We are web developers based in Stockton, CA, USA. Most of our projects go through the same process. Understanding this process may help you win a project with us. We custom-code all of our websites in-house. We don’t have any requirements as to what tools you use for your design, but we prefer Figma files. For any design that we label as four-stars, we send it to the client for review. The client picks the final design they want us to use. Once we complete this process, we will continue to show additional clients all the four-star sites and purchase them later. Your designs will have multiple chances to sell. For better chances of success, we ask that you follow these guidelines.

IMAGES:
If you use any images or icons in the design, we ask that you have a link to the asset so we can purchase the image/icon. Most of the designs we submit do not have the customer’s images on them unless they have some great images. Be creative; show us the feeling you are trying to portray with your image choices. Use any royalty-free site you choose. We subscribe to Varnex and mainly use their images, but we can purchase images outside of Varnex.

PLEASE NOTE: we will not submit designs to clients with watermarks on the images.

FONTS:
We ask that you identify the fonts used in the design. This can be done in a message if you want. We typically use Google Fonts and Varnex Fonts.

CONTENT:
We're always open to different content and ideas. We often submit designs with stock images so the client can see our vision. We typically take pictures after the website launch to use their images with our vision. Lorem Ipsum is fine for paragraphs, but we ask that you write the headers in correct English. We want to be able to show the vision and identify the sections of the website.

INSPIRATION:
We typically add a couple of links in the brief of websites we like to help you get started in your design.

REVISIONS:
We do not often ask for revisions of the designs unless we see something in the design that may not appeal to the client. If there are slight changes that we want to make, we do that in the development process.

FEEDBACK:
We rarely give feedback on designs during the design process. We are working on many website projects and do not have the time to provide feedback. We usually respond if your request is well thought out and asks specific questions, but a note asking “feedback, please” usually goes unanswered.

```html
<!DOCTYPE html>
<html lang="en">
<head>
<meta charset="utf-8">
<title>Fernhollow Co — Home</title>
<link rel="stylesheet" href="https://fonts.googleapis.com/css2?family=Libre+Baskerville:wght@400;700&family=Montserrat:wght@400;500;600;700&display=swap">
<style>
:root{
  --blue:#1f6fb5;
  --navy:#1b4a93;
  --pink:#e8157c;
  --ink:#1c1c1c;
  --muted:#4a4a4a;
  --sky:#dfe7ef;
  --footer:#1f1f23;
  --gold:#f2b01e;
  --grad:linear-gradient(90deg,#1d5fa8 0%,#e8157c 100%);
  --serif:"Libre Baskerville",Georgia,serif;
  --sans:"Montserrat",Arial,sans-serif;
}
*{box-sizing:border-box;margin:0;padding:0}
html,body{width:1200px;height:4608px;overflow:hidden;background:#fff}
body{font-family:var(--sans);color:var(--ink);position:relative}
.abs{position:absolute}
svg{display:block}

/* header */
.topbar{left:599px;top:0;width:601px;height:43px;background:var(--pink);border-bottom-left-radius:22px;display:flex;align-items:center;gap:54px;padding-left:48px;color:#fff;font-size:13px}
.topbar span{display:flex;align-items:center;gap:12px}
.topbar .ico{width:28px;height:28px;border:1.5px solid #fff;border-radius:50%;display:flex;align-items:center;justify-content:center}
.brand{display:flex;align-items:center;gap:12px;font-family:var(--sans);font-weight:700;color:var(--blue);font-size:30px}
.brand .dot{width:34px;height:34px;border-radius:50%;background:#8fc6ec}
.header-brand{left:113px;top:48px}
.nav{left:418px;top:76px;display:flex;gap:40px;font-size:12px;font-weight:500;letter-spacing:.3px}
.nav .active{color:var(--pink);font-weight:700}
.tools{left:950px;top:70px;display:flex;gap:20px;align-items:center}
.cart{position:relative}
.cart b{position:absolute;top:-8px;right:-10px;width:17px;height:17px;border-radius:50%;background:#35a9e0;color:#fff;font-size:10px;display:flex;align-items:center;justify-content:center}

/* hero */
.hero{left:0;top:127px;width:1200px;height:540px;overflow:hidden}
.hero-photo{position:absolute;inset:0;background:linear-gradient(100deg,#1d4f92 0%,#3a6fb0 40%,#8a4f9a 75%,#c43878 100%)}
.hero-copy{left:111px;top:222px;color:#fff}
.hero-copy .kicker{font-family:var(--serif);font-size:24px}
.hero-copy h1{font-family:var(--serif);font-weight:400;font-size:50px;margin-top:14px;letter-spacing:1px}
.hero-copy p{font-size:16px;line-height:33px;width:490px;margin-top:18px}
.btn-outline{display:inline-block;margin-top:20px;border:2px solid #fff;border-radius:24px;padding:11px 28px;font-size:14px;font-weight:700;color:#fff}

/* headings */
.h2{font-family:var(--serif);font-size:36px;font-weight:400;letter-spacing:.5px}
.center{left:0;width:1200px;text-align:center}

/* categories */
.view-all{left:1005px;top:748px;font-size:14px;font-weight:700;text-decoration:underline;color:var(--navy)}
.cat{width:227px;text-align:center}
.cat .photo{width:227px;height:227px;border-radius:50%}
.cat p{margin-top:32px;font-size:23px;font-weight:500}

/* about */
.about-ring{left:123px;top:1212px;width:454px;height:454px;border-radius:50%;background:linear-gradient(135deg,#7fa6d8,#e476b8);padding:5px}
.about-ring div{width:100%;height:100%;border-radius:50%;background:linear-gradient(120deg,#6d8c6a 0%,#4f7fc2 45%,#cfe0f2 100%);border:6px solid #fff}
.about-copy{left:653px;top:1270px;width:410px}
.about-copy p{font-size:14px;line-height:27.5px;color:var(--muted);margin-top:30px}
.btn-grad{display:inline-block;background:var(--grad);color:#fff;font-weight:700;border-radius:24px;text-align:center}
.about-copy .btn-grad{margin-top:36px;width:191px;height:45px;line-height:45px;font-size:15px}

/* why */
.why-bg{left:0;top:1700px;width:1200px;height:950px}
.svc{font-size:20px;font-weight:600;line-height:36px}
.svc-ico{width:84px;height:84px;border-radius:50%;background:#fff;border:2px solid #c58ac7;display:flex;align-items:center;justify-content:center}
.why-photo{left:500px;top:1985px;width:190px;height:380px;border-radius:12px;background:linear-gradient(180deg,#9aa3ae 0%,#5d6570 50%,#3a4049 100%)}

/* products */
.card{width:304px;height:385px;background:#fff;box-shadow:0 2px 12px rgba(0,0,0,.18);text-align:center}
.card .photo{height:192px}
.card h3{margin-top:24px;font-size:18px;font-weight:700;color:var(--pink)}
.card .rate{margin-top:12px;font-size:12px;color:#555;display:flex;justify-content:center;align-items:center;gap:14px}
.card .rate i{font-style:normal;color:var(--gold);font-size:17px;letter-spacing:1px}
.card .price{margin-top:10px;font-size:19px}
.card .price s{color:#333}
.card .btn-grad{margin-top:16px;width:124px;height:32px;line-height:32px;font-size:10px}
.arrow{width:38px;height:38px;border-radius:50%;border:2px solid #888;display:flex;align-items:center;justify-content:center;background:#fff}

/* contact */
.contact-bg{left:0;top:3308px;width:1200px;height:800px;background:var(--sky)}
.info{display:flex;gap:14px}
.info h4{font-size:21px;font-weight:700}
.info p{font-size:21px;line-height:32px}
.field{border:1.5px solid #8a8a8a;border-radius:28px;background:#fff;font-size:14px;padding:0 22px;display:flex;align-items:center}
.field.msg{align-items:flex-start;padding-top:26px;border-radius:24px}
.map{left:613px;top:3615px;width:462px;height:376px;border:4px solid #e06db0;border-radius:8px;background:linear-gradient(135deg,#e9e4d2,#d7e3c8 55%,#c9d9b7)}
.map span{position:absolute;left:170px;top:190px;font-size:19px;font-weight:700}

/* footer */
.footer{left:0;top:4150px;width:1200px;height:458px;background:var(--footer)}
.f-col{color:#fff}
.f-col h5{font-size:17px;font-weight:700;line-height:28px}
.f-col ul{list-style:none;margin-top:28px;font-size:14px;line-height:27px}
.newsletter{left:874px;top:4361px;width:213px;height:43px;background:#fff;border-radius:6px;display:flex;align-items:center;justify-content:space-between;color:#333;font-size:12px;padding-left:10px}
.newsletter b{width:42px;height:39px;margin-right:2px;background:#2a86c8;border-radius:5px;display:flex;align-items:center;justify-content:center}
.divider{left:109px;top:4536px;width:975px;height:1px;background:#888}
.copy{top:4565px;font-size:12px;color:#ddd}
</style>
</head>
<body>

<!-- Header -->
<div class="abs topbar">
  <span><i class="ico"><svg width="14" height="14" viewBox="0 0 24 24" fill="none" stroke="#fff" stroke-width="2"><path d="M5 3h4l2 5-3 2a11 11 0 0 0 6 6l2-3 5 2v4a2 2 0 0 1-2 2A17 17 0 0 1 3 5a2 2 0 0 1 2-2z"/></svg></i>+1 555 010 2040</span>
  <span><i class="ico"><svg width="14" height="14" viewBox="0 0 24 24" fill="none" stroke="#fff" stroke-width="2"><rect x="3" y="5" width="18" height="14" rx="2"/><path d="M3 7l9 6 9-6"/></svg></i>info@fernhollowco.com</span>
</div>
<div class="abs brand header-brand"><i class="dot"></i>Fernhollow Co</div>
<nav class="abs nav"><span class="active">HOME</span><span>ABOUT US</span><span>OUR PRODUCT</span><span>BLOGS</span><span>CONTACT US</span></nav>
<div class="abs tools">
  <svg width="28" height="28" viewBox="0 0 24 24" fill="none" stroke="#222" stroke-width="1.6"><circle cx="12" cy="12" r="10"/><circle cx="12" cy="10" r="3.5"/><path d="M5.5 18.5c2-3 11-3 13 0"/></svg>
  <svg width="26" height="26" viewBox="0 0 24 24" fill="none" stroke="#222" stroke-width="2"><circle cx="10" cy="10" r="7"/><path d="M15 15l6 6"/></svg>
  <span class="cart"><svg width="28" height="26" viewBox="0 0 24 24" fill="none" stroke="#222" stroke-width="1.8"><path d="M2 3h3l3 12h11l2-8H6"/><circle cx="9" cy="20" r="1.5"/><circle cx="18" cy="20" r="1.5"/></svg><b>0</b></span>
</div>

<!-- Hero -->
<section class="abs hero">
  <div class="hero-photo" role="img" aria-label="Shopper reaching for bottled water on a supermarket shelf"></div>
  <svg class="abs" style="left:0;bottom:0" width="1200" height="200" viewBox="0 0 1200 200" preserveAspectRatio="none">
    <defs><linearGradient id="rib" x1="0" x2="1"><stop offset="0" stop-color="#1d5fa8"/><stop offset=".55" stop-color="#4a3f9c"/><stop offset="1" stop-color="#e8157c"/></linearGradient></defs>
    <path d="M0 200 L0 120 C200 20 380 60 560 110 C760 165 960 150 1200 90 L1200 200 Z" fill="url(#rib)"/>
    <path d="M0 200 L0 150 C200 60 380 80 560 130 C760 185 960 170 1200 110 L1200 200 Z" fill="#fff"/>
  </svg>
</section>
<div class="abs hero-copy">
  <div class="kicker">WELCOME TO</div>
  <h1>FERNHOLLOW CO</h1>
  <p>Lorem Ipsum is simply dummy text of the printing and typesetting industry.</p>
  <span class="btn-outline">GET STARTED</span>
</div>

<!-- Categories -->
<h2 class="abs h2" style="left:111px;top:737px">SHOP BY CATEGORIES</h2>
<span class="abs view-all">VIEW ALL</span>
<div class="abs cat" style="left:113px;top:824px"><div class="photo" role="img" aria-label="Large blue water jugs in a warehouse" style="background:radial-gradient(circle,#5d9be0,#1f56a8)"></div><p>Lorem ipsum</p></div>
<div class="abs cat" style="left:362px;top:824px"><div class="photo" role="img" aria-label="Single clear plastic water bottle" style="background:radial-gradient(circle,#f4f5f6,#c9ccd0)"></div><p>Lorem ipsum</p></div>
<div class="abs cat" style="left:608px;top:824px"><div class="photo" role="img" aria-label="Blue capped water bottles stacked together" style="background:radial-gradient(circle,#4c9de6,#0e4d9c)"></div><p>Lorem ipsum</p></div>
<div class="abs cat" style="left:859px;top:824px"><div class="photo" role="img" aria-label="Rows of teal water bottles" style="background:radial-gradient(circle,#7dd0d8,#2b8eaa)"></div><p>Lorem ipsum</p></div>

<!-- About -->
<div class="abs about-ring"><div role="img" aria-label="Woman picking bottled water from a store shelf"></div></div>
<div class="abs about-copy">
  <h2 class="h2">ABOUT US</h2>
  <p>Lorem Ipsum is simply dummy text of the printing and typesetting industry. Lorem Ipsum has been the industry's standard dummy text ever since the 1500s, when an unknown printer took a galley of type and scrambled it to make a type specimen book. It has survived not only five centuries, but also the leap into electronic typesetting, remaining essentially</p>
  <span class="btn-grad">READ MORE</span>
</div>

<!-- Why choose us -->
<svg class="abs why-bg" viewBox="0 0 1200 950" preserveAspectRatio="none" role="img" aria-label="Soft faded background of water bottles on shelves">
  <defs><linearGradient id="whyg" x1="0" y1="0" x2="0" y2="1"><stop offset="0" stop-color="#d7e3ee"/><stop offset="1" stop-color="#cbdbe9"/></linearGradient></defs>
  <path d="M0 60 C250 0 500 40 720 50 C900 58 1050 20 1200 10 L1200 880 C1000 900 800 930 560 935 C330 940 150 900 0 880 Z" fill="url(#whyg)"/>
</svg>
<h2 class="abs h2 center" style="top:1848px">WHY CHOOSE US</h2>
<svg class="abs" style="left:373px;top:1950px" width="440" height="440" viewBox="0 0 440 440">
  <defs><linearGradient id="ring" x1="0" y1="0" x2="1" y2="1"><stop offset="0" stop-color="#5a7fc4"/><stop offset="1" stop-color="#e8157c"/></linearGradient></defs>
  <circle cx="220" cy="220" r="213" fill="#ced6e0" stroke="url(#ring)" stroke-width="6"/>
</svg>
<div class="abs why-photo" role="img" aria-label="Photo of a dark water bottle with a blank label"></div>

<div class="abs svc-ico" style="left:367px;top:2023px"><svg width="40" height="40" viewBox="0 0 24 24" fill="none" stroke="#7a3a8a" stroke-width="1.4"><rect x="5" y="3" width="14" height="18" rx="2"/><path d="M5 9h14M9 13h6v4H9z"/></svg></div>
<div class="abs svc-ico" style="left:736px;top:2023px"><svg width="40" height="40" viewBox="0 0 24 24" fill="none" stroke="#7a3a8a" stroke-width="1.4"><rect x="3" y="9" width="18" height="11" rx="2"/><path d="M7 9V5M12 9V5M17 9V5"/><circle cx="8" cy="14" r="1"/><circle cx="12" cy="15" r="1"/><circle cx="16" cy="14" r="1"/></svg></div>
<div class="abs svc-ico" style="left:382px;top:2247px"><svg width="40" height="40" viewBox="0 0 24 24" fill="none" stroke="#7a3a8a" stroke-width="1.4"><path d="M8 3v9a4 4 0 0 0 8 0V3"/><circle cx="15" cy="15" r="4"/><path d="M18 18l3 3"/></svg></div>
<div class="abs svc-ico" style="left:723px;top:2247px"><svg width="40" height="40" viewBox="0 0 24 24" fill="none" stroke="#7a3a8a" stroke-width="1.4"><rect x="4" y="9" width="16" height="12" rx="1"/><path d="M7 9V4h10v5M9 14h6"/></svg></div>
<div class="abs svc-ico" style="left:552px;top:2329px"><svg width="40" height="40" viewBox="0 0 24 24" fill="none" stroke="#7a3a8a" stroke-width="1.4"><rect x="3" y="7" width="15" height="11" rx="1"/><path d="M6 7v11M10 7v11M14 7v11M18 10h3v5h-3"/></svg></div>

<div class="abs svc" style="left:111px;top:2024px">Water Coolers and<br>Dispensers</div>
<div class="abs svc" style="left:844px;top:2033px">Bottled Water Sales</div>
<div class="abs svc" style="left:140px;top:2269px;width:176px;text-align:right">Water Testing<br>Services</div>
<div class="abs svc" style="left:840px;top:2274px">Water Delivery Services</div>
<div class="abs svc" style="left:494px;top:2430px;width:200px;text-align:center">Water Filtration<br>Systems</div>

<!-- Products -->
<h2 class="abs h2 center" style="top:2731px">OUR PRODUCTS</h2>
<div class="abs arrow" style="left:22px;top:3001px"><svg width="16" height="16" viewBox="0 0 24 24" fill="none" stroke="#555" stroke-width="2.5"><path d="M15 5l-7 7 7 7"/></svg></div>
<div class="abs arrow" style="left:1111px;top:3001px;border-color:#7a3a8a"><svg width="16" height="16" viewBox="0 0 24 24" fill="none" stroke="#7a3a8a" stroke-width="2.5"><path d="M9 5l7 7-7 7"/></svg></div>

<div class="abs card" style="left:107px;top:2823px">
  <div class="photo" role="img" aria-label="Blue water cooler jugs lined up" style="background:linear-gradient(180deg,#3d7fd0,#0f3f8a)"></div>
  <h3>FERNHOLLOW CO</h3>
  <div class="rate"><i>★★★★★</i>127 Reviews</div>
  <div class="price">Price at <s>$15.99</s> $13.99</div>
  <span class="btn-grad">READ MORE</span>
</div>
<div class="abs card" style="left:438px;top:2823px">
  <div class="photo" role="img" aria-label="Dark bottle with blank white label" style="background:linear-gradient(180deg,#dfe4ea,#b8c1cc)"></div>
  <h3>FERNHOLLOW CO</h3>
  <div class="rate"><i>★★★★★</i>127 Reviews</div>
  <div class="price">Price at <s>$15.99</s> $13.99</div>
  <span class="btn-grad">READ MORE</span>
</div>
<div class="abs card" style="left:780px;top:2823px">
  <div class="photo" role="img" aria-label="Clear plastic water bottle on light background" style="background:linear-gradient(180deg,#eceef0,#c9cdd2)"></div>
  <h3>FERNHOLLOW CO</h3>
  <div class="rate"><i>★★★★★</i>127 Reviews</div>
  <div class="price">Price at <s>$15.99</s> $13.99</div>
  <span class="btn-grad">READ MORE</span>
</div>

<!-- Contact -->
<div class="abs contact-bg"></div>
<h2 class="abs h2 center" style="top:3398px">CONTACT US</h2>
<div class="abs info" style="left:143px;top:3493px">
  <svg width="32" height="32" viewBox="0 0 24 24" fill="var(--navy)"><path d="M12 2a6 6 0 0 0-6 6c0 4.5 6 11 6 11s6-6.5 6-11a6 6 0 0 0-6-6zm0 8a2 2 0 1 1 0-4 2 2 0 0 1 0 4z"/><ellipse cx="12" cy="21" rx="7" ry="1.6" fill="none" stroke="var(--navy)" stroke-width="1.5"/></svg>
  <div><h4>HEAD OFFICE</h4><p>26, 7047 Lorem Ipsum<br>is simply dummy text</p></div>
</div>
<div class="abs info" style="left:474px;top:3493px">
  <svg width="30" height="30" viewBox="0 0 24 24" fill="none" stroke="var(--navy)" stroke-width="2"><path d="M5 3h4l2 5-3 2a11 11 0 0 0 6 6l2-3 5 2v4a2 2 0 0 1-2 2A17 17 0 0 1 3 5a2 2 0 0 1 2-2z"/></svg>
  <div><h4>CALL US</h4><p>+1 555 010 2040</p></div>
</div>
<div class="abs info" style="left:773px;top:3493px">
  <svg width="34" height="30" viewBox="0 0 24 24" fill="none" stroke="var(--navy)" stroke-width="2"><rect x="2" y="5" width="20" height="14" rx="1"/><path d="M2 5l10 8 10-8M2 19l7-7M22 19l-7-7"/></svg>
  <div><h4>MAIL US</h4><p>info@fernhollowco.com</p></div>
</div>

<div class="abs field" style="left:111px;top:3626px;width:234px;height:54px">Name</div>
<div class="abs field" style="left:354px;top:3626px;width:234px;height:54px">Phone Number</div>
<div class="abs field" style="left:111px;top:3694px;width:234px;height:54px">Email Address</div>
<div class="abs field" style="left:354px;top:3694px;width:234px;height:54px">Address</div>
<div class="abs field" style="left:111px;top:3762px;width:477px;height:54px">Subject</div>
<div class="abs field msg" style="left:111px;top:3830px;width:477px;height:115px">Your Message</div>
<span class="abs btn-grad" style="left:118px;top:3968px;width:191px;height:44px;line-height:44px;font-size:15px">SUBMIT</span>

<div class="abs map" role="img" aria-label="Street map showing the store location">
  <svg class="abs" style="left:238px;top:150px" width="26" height="32" viewBox="0 0 24 30"><path d="M12 1a9 9 0 0 0-9 9c0 7 9 18 9 18s9-11 9-18a9 9 0 0 0-9-9z" fill="var(--pink)"/><circle cx="12" cy="10" r="3.5" fill="#fff"/></svg>
  <span>FERNHOLLOW CO</span>
</div>

<!-- Footer -->
<svg class="abs" style="left:0;top:4080px" width="1200" height="140" viewBox="0 0 1200 140" preserveAspectRatio="none">
  <path d="M0 40 C160 0 300 20 460 60 C700 120 950 100 1200 30 L1200 140 L0 140 Z" fill="url(#rib)"/>
  <path d="M0 70 C160 30 300 45 460 85 C700 140 950 120 1200 60 L1200 140 L0 140 Z" fill="var(--footer)"/>
</svg>
<footer class="abs footer"></footer>
<div class="abs brand" style="left:113px;top:4310px;color:#4aa3e0"><i class="dot"></i>Fernhollow Co</div>
<div class="abs f-col" style="left:417px;top:4286px"><h5>MAIN LINKS</h5><ul><li>Home</li><li>About Us</li><li>Our Product</li><li>Blogs</li><li>Contact Us</li></ul></div>
<div class="abs f-col" style="left:628px;top:4286px"><h5>NEED HELP?</h5><ul><li>Email Us</li><li>My Account</li><li>Privacy Policy</li><li>Terms and Conditions</li></ul></div>
<div class="abs f-col" style="left:876px;top:4286px"><h5>SIGN UP FOR OUR<br>MONTHLY NEWSLETTER!</h5></div>
<div class="abs newsletter">Your Email Address<b><svg width="20" height="20" viewBox="0 0 24 24" fill="none" stroke="#fff" stroke-width="1.8"><path d="M22 2L2 10l8 3 3 8z M22 2L10 13"/></svg></b></div>
<div class="abs divider"></div>
<div class="abs copy center">© 2024 Fernhollow Co | All Rights Reserved</div>

</body>
</html>
```